Consulting company business cards

We have a base design, but would be willing to update. We have a new logo/"tag" that needs to be added. Current business card design is attached for reference into our "style."

Industry/Entity Type

Business

Contact Information for Business Card

Should contain name and title, office number, mobile number if appropriate, e-mail, website, physical address, and company logo.

Font styles to use
Other font styles liked:
• See current card design on GorvandBCard

Colors
0455a3
85acd3
aaaaaa

Requirements
Must have
• Our colors are navy blue, gray, and a lighter blue
Nice to have
• Design that I can easily drop in new names/titles as we hire employees.

```html
<!DOCTYPE html>
<html lang="en">
<head>
<meta charset="utf-8">
<title>Tessaro Business Cards</title>
<link rel="stylesheet" href="https://fonts.googleapis.com/css2?family=Arimo:wght@400;700&display=swap">
<style>
  :root {
    --backdrop: #3a3330;
    --card: #141517;
    --brand-blue: #0455a3;
    --light-blue: #85acd3;
    --mid-blue: #2d78b4;
    --gray: #aaaaaa;
    --text: #e9e9e9;
    --rule: #55585c;
  }
  * { margin: 0; padding: 0; box-sizing: border-box; }
  html, body {
    width: 1200px; height: 864px; overflow: hidden;
    background: var(--backdrop);
    font-family: "Arimo", Arial, sans-serif;
  }
  .canvas { position: relative; width: 1200px; height: 864px; }
  .card {
    position: absolute; width: 540px; height: 309px;
    background: var(--card);
    border-radius: 3px;
    box-shadow: 0 8px 24px rgba(0,0,0,.45);
  }
  .card-front { left: 60px; top: 120px; }
  .card-back { left: 600px; top: 420px; }

  .brand-name {
    font-family: "Arimo", Arial, sans-serif; font-weight: 700;
    line-height: 1; letter-spacing: 0.5px;
  }
  .brand-dot { display: block; border-radius: 50%; background: var(--light-blue); flex: none; }

  /* front */
  .front-mark {
    position: absolute; left: 0; right: 0; top: 84px;
    display: flex; align-items: center; justify-content: center; gap: 16px;
  }
  .front-mark .brand-name { font-size: 48px; color: var(--light-blue); }
  .front-mark .brand-dot { width: 40px; height: 40px; }
  .front-web {
    position: absolute; left: 0; right: 0; bottom: 52px; text-align: center;
    font-size: 14px; letter-spacing: 5px; color: var(--text);
  }

  /* back */
  .logo-block { position: absolute; right: 40px; top: 40px; }
  .logo-row { display: flex; align-items: center; justify-content: flex-end; gap: 12px; }
  .logo-row .brand-name { font-size: 40px; color: var(--brand-blue); }
  .logo-row .brand-dot { width: 32px; height: 32px; }
  .tagline {
    font-size: 13px; letter-spacing: 1.5px; color: var(--gray);
    margin-top: 8px; text-align: right;
  }

  .details {
    position: absolute; left: 40px; right: 40px; top: 158px;
    display: flex; justify-content: flex-end; gap: 22px;
  }
  .person { text-align: right; font-size: 14px; line-height: 19px; color: var(--text); }
  .person-name { color: var(--mid-blue); font-size: 17px; line-height: 22px; }
  .person-title { color: var(--light-blue); font-size: 15px; }
  .divider { width: 1px; background: var(--rule); }
  .contacts { list-style: none; font-size: 14px; line-height: 22px; color: var(--text); }
  .contacts li { display: flex; align-items: center; gap: 10px; }
  .contacts svg { width: 13px; height: 13px; fill: var(--mid-blue); flex: none; }
</style>
</head>
<body>
<main class="canvas">
  <section class="card card-front">
    <div class="front-mark">
      <span class="brand-dot"></span>
      <span class="brand-name">Tessaro</span>
    </div>
    <p class="front-web">www.tessarocloud.net</p>
  </section>

  <section class="card card-back">
    <div class="logo-block">
      <div class="logo-row">
        <span class="brand-name">Tessaro</span>
        <span class="brand-dot"></span>
      </div>
      <p class="tagline">A CLOUD CONSULTING COMPANY</p>
    </div>

    <div class="details">
      <div class="person">
        <p class="person-name">Nadia Gorvand</p>
        <p class="person-title">Office Manager</p>
        <p>1873 W 54th ST</p>
        <p>Brookfield Ohio 44403</p>
      </div>
      <div class="divider"></div>
      <ul class="contacts">
        <li><svg viewBox="0 0 16 16"><path d="M3 1h3l1.5 4-2 1.3a9 9 0 0 0 4.2 4.2L11 8.5l4 1.5v3a2 2 0 0 1-2 2A12 12 0 0 1 1 3a2 2 0 0 1 2-2z"/></svg>555.014.2283</li>
        <li><svg viewBox="0 0 16 16"><rect x="4" y="1" width="8" height="14" rx="1.5"/></svg>555.014.2291</li>
        <li><svg viewBox="0 0 16 16"><path d="M1 3h14v10H1z M1 3l7 6 7-6" stroke="#141517" stroke-width="1"/></svg>ngorvand@tessarocloud.net</li>
        <li><svg viewBox="0 0 16 16"><circle cx="8" cy="8" r="7"/></svg>www.tessarocloud.net</li>
      </ul>
    </div>
  </section>
</main>
</body>
</html>
```